Bright Towns Alliance PowerPoint Design Template and Sample Deck

The Bright Towns Alliance is an international organization that seeks to improve the livability, workability and sustainability of the world’s cities.
We seek a versatile PowerPoint design template with 10 slide types plus a “self-documenting” sample deck. Your design will be used in keynote speeches and workshops around the world.
After the contest is completed, we will ask the winning designer to add 10-20 additional slide types for $75 per slide. We also seek a long-term relationship whereby we can request “custom” slides and/or ask the designer to touch up the slides we build to make them better.
FILES. We have uploaded several files:
2. PALETTE. Shows our official colors.
3 LOGOS. Several individual files with different variations of our logo. Some with our motto, some without.
2. SAMPLE SLIDES. Because we were unable to successfully upload our sample deck, we are making it available via this FileCrate link:
https://www.filecrate-example.net/s/q7mrk2tzw9hdn4e/The%20Bright%20Towns%20Alliance%20Design%20Contest%20Notes.docx?dl=0
Target Market(s)
Mayors, department heads, CIOs, senior executives from technology companies
Industry/Entity Type
Information Technology
Colors
Designer to choose colors to be used in the design.
Requirements
Must have
- Please see uploaded Word document for requirements, nice to haves and should not haves and uploaded palette for color preferences.
Nice to have
- see above
Should not have
- see above

```html
<!DOCTYPE html>
<html lang="en">
<head>
<meta charset="utf-8">
<title>Bright Towns Alliance – Slide Template Overview</title>
<link href="https://fonts.googleapis.com/css2?family=Lato:wght@400;700;900&display=swap" rel="stylesheet">
<style>
  :root{
    --navy:#0d2b57;
    --blue:#1c4f9c;
    --orange:#f7941d;
    --red:#ef4b2a;
    --green:#7fa13a;
    --purple:#8a44a8;
    --grey:#9aa1ab;
    --light:#e9ebee;
    --ink:#3c4250;
  }
  html,body{margin:0;padding:0;}
  body{width:810px;height:1200px;overflow:hidden;background:#fff;font-family:"Lato",sans-serif;position:relative;}
  .slide{position:absolute;width:259px;height:145px;box-shadow:0 1px 3px rgba(0,0,0,.25);background:#fff;overflow:hidden;}
  .slide svg{display:block;width:100%;height:100%;}
  .slide text{font-family:"Lato",sans-serif;}
  .c1{left:5.6px}.c2{left:275px}.c3{left:544.6px}
  .r1{top:3px}.r2{top:153px}.r3{top:303px}.r4{top:453px}.r5{top:603px}.r6{top:753px}.r7{top:902px}.r8{top:1052px;height:146px}
  .title{font-size:10.5px;font-weight:700;fill:var(--navy);}
  .tiny{font-size:3.2px;fill:#7a808c;}
  .small{font-size:4px;fill:var(--ink);}
  .foot-brand{font-size:4px;font-weight:700;fill:#fff;}
  .foot-copy{font-size:3.2px;fill:#fff;}
</style>
</head>
<body>
<svg width="0" height="0" style="position:absolute">
  <defs>
    <g id="footer">
      <rect x="0" y="171" width="322" height="9" fill="#0d2b57"/>
      <text x="10" y="177.3" class="foot-brand">Bright Towns Alliance</text>
      <text x="306" y="177.3" class="foot-copy" text-anchor="end">© 2017 Bright Towns Alliance. All rights reserved.</text>
      <rect x="311" y="171" width="11" height="9" fill="#f7941d"/>
    </g>
    <rect id="tbar" x="0" y="7" width="2" height="11" fill="#f7941d"/>
  </defs>
</svg>

<!-- Row 1 -->
<section class="slide c1 r1" aria-label="Timeline 1 Year">
<svg viewBox="0 0 322 180">
  <use href="#tbar"/><text x="8" y="16.5" class="title">Timeline 1 Year</text>
  <g class="tiny">
    <text x="40" y="48">Project step</text>
    <text x="88" y="48">Jan</text><text x="106" y="48">Feb</text><text x="124" y="48">Mar</text><text x="142" y="48">Apr</text><text x="160" y="48">May</text><text x="178" y="48">June</text><text x="196" y="48">July</text><text x="214" y="48">Aug</text><text x="232" y="48">Sep</text><text x="250" y="48">Oct</text><text x="268" y="48">Nov</text><text x="286" y="48">Dec</text>
    <text x="42" y="58">Process 01</text><text x="42" y="67">Process 02</text><text x="42" y="76">Process 03</text><text x="42" y="85">Process 04</text><text x="42" y="94">Process 05</text><text x="42" y="103">Process 06</text><text x="42" y="112">Process 07</text><text x="42" y="121">Process 08</text><text x="42" y="130">Process 09</text>
  </g>
  <g stroke="#dfe2e6" stroke-width=".4">
    <line x1="38" y1="51" x2="296" y2="51"/><line x1="38" y1="60" x2="296" y2="60"/><line x1="38" y1="69" x2="296" y2="69"/><line x1="38" y1="78" x2="296" y2="78"/><line x1="38" y1="87" x2="296" y2="87"/><line x1="38" y1="96" x2="296" y2="96"/><line x1="38" y1="105" x2="296" y2="105"/><line x1="38" y1="114" x2="296" y2="114"/><line x1="38" y1="123" x2="296" y2="123"/><line x1="38" y1="132" x2="296" y2="132"/>
  </g>
  <g stroke-linecap="round" stroke-width="3.5">
    <line x1="92" y1="56" x2="128" y2="56" stroke="#0d2b57"/><line x1="250" y1="56" x2="290" y2="56" stroke="#0d2b57"/>
    <line x1="112" y1="65" x2="130" y2="65" stroke="#ef4b2a"/><line x1="170" y1="65" x2="196" y2="65" stroke="#1c4f9c"/>
    <line x1="134" y1="74" x2="226" y2="74" stroke="#f7941d"/><line x1="236" y1="74" x2="252" y2="74" stroke="#ef4b2a"/>
    <line x1="148" y1="83" x2="170" y2="83" stroke="#7fa13a"/><line x1="226" y1="83" x2="248" y2="83" stroke="#7fa13a"/>
    <line x1="176" y1="92" x2="292" y2="92" stroke="#8a44a8"/>
    <line x1="148" y1="101" x2="180" y2="101" stroke="#0d2b57"/>
    <line x1="196" y1="110" x2="210" y2="110" stroke="#f7941d"/><line x1="238" y1="110" x2="270" y2="110" stroke="#1c4f9c"/>
  </g>
  <g class="tiny">
    <circle cx="62" cy="151" r="1.5" fill="#0d2b57"/><text x="66" y="152">Description</text>
    <circle cx="100" cy="151" r="1.5" fill="#ef4b2a"/><text x="104" y="152">Description</text>
    <circle cx="140" cy="151" r="1.5" fill="#1c4f9c"/><text x="144" y="152">Description</text>
    <circle cx="180" cy="151" r="1.5" fill="#f7941d"/><text x="184" y="152">Description</text>
    <circle cx="220" cy="151" r="1.5" fill="#7fa13a"/><text x="224" y="152">Description</text>
    <circle cx="260" cy="151" r="1.5" fill="#8a44a8"/><text x="264" y="152">Description</text>
  </g>
  <use href="#footer"/>
</svg>
</section>

<section class="slide c2 r1" aria-label="Timeline 6 month">
<svg viewBox="0 0 322 180">
  <use href="#tbar"/><text x="8" y="16.5" class="title">Timeline 6 month</text>
  <g font-size="3.6" fill="#fff" font-weight="700" text-anchor="middle">
    <rect x="42" y="44" width="43" height="9" fill="#0d2b57"/><text x="63.5" y="50">January</text>
    <rect x="85" y="44" width="43" height="9" fill="#ef4b2a"/><text x="106.5" y="50">February</text>
    <rect x="128" y="44" width="43" height="9" fill="#1c4f9c"/><text x="149.5" y="50">March</text>
    <rect x="171" y="44" width="43" height="9" fill="#f7941d"/><text x="192.5" y="50">April</text>
    <rect x="214" y="44" width="43" height="9" fill="#7fa13a"/><text x="235.5" y="50">May</text>
    <rect x="257" y="44" width="45" height="9" fill="#8a44a8"/><text x="279.5" y="50">June</text>
  </g>
  <g fill="#a2a8b1">
    <rect x="10" y="58" width="292" height="8"/><rect x="10" y="70" width="292" height="8"/><rect x="10" y="82" width="292" height="8"/><rect x="10" y="94" width="292" height="8"/><rect x="10" y="106" width="292" height="8"/><rect x="10" y="118" width="292" height="8"/><rect x="10" y="130" width="292" height="8"/>
  </g>
  <g font-size="3" fill="#fff">
    <text x="13" y="63">Step One</text><text x="13" y="75">Step Two</text><text x="13" y="87">Step Three</text><text x="13" y="99">Step Four</text><text x="13" y="111">Step Five</text><text x="13" y="123">Step Six</text><text x="13" y="135">Step Seven</text>
  </g>
  <g font-size="3" fill="#fff" text-anchor="middle">
    <path d="M45 59h72l4 3-4 3h-72z" fill="#0d2b57"/><text x="82" y="63">Description</text>
    <path d="M100 71h62l4 3-4 3h-62z" fill="#ef4b2a"/><text x="132" y="75">Description</text>
    <path d="M130 83h84l4 3-4 3h-84z" fill="#0d2b57"/><text x="172" y="87">Description</text>
    <path d="M100 95h52l4 3-4 3h-52z" fill="#0d2b57"/><text x="126" y="99">Description</text>
    <path d="M170 107h80l4 3-4 3h-80z" fill="#f7941d"/><text x="210" y="111">Description</text>
    <path d="M220 119h62l4 3-4 3h-62z" fill="#ef4b2a"/><text x="251" y="123">Description</text>
    <path d="M240 131h62v6h-62z" fill="#0d2b57"/><text x="271" y="135">Description</text>
  </g>
  <g class="tiny" text-anchor="middle">
    <rect x="112" y="148" width="3" height="3" fill="#0d2b57"/><text x="113.5" y="156">Description</text>
    <rect x="140" y="148" width="3" height="3" fill="#ef4b2a"/><text x="141.5" y="156">Description</text>
    <rect x="168" y="148" width="3" height="3" fill="#1c4f9c"/><text x="169.5" y="156">Description</text>
    <rect x="196" y="148" width="3" height="3" fill="#f7941d"/><text x="197.5" y="156">Description</text>
  </g>
  <use href="#footer"/>
</svg>
</section>

<section class="slide c3 r1" aria-label="Linear Process 4 Steps">
<svg viewBox="0 0 322 180">
  <use href="#tbar"/><text x="8" y="16.5" class="title">Linear Process 4 Steps</text>
  <path d="M50 87h50l5 4-5 4h-50z" fill="#0d2b57"/>
  <path d="M105 87h55l5 4-5 4h-55z" fill="#ef4b2a"/>
  <path d="M165 87h55l5 4-5 4h-55z" fill="#1c4f9c"/>
  <path d="M225 87h60l5 4-5 4h-60z" fill="#f7941d"/>
  <line x1="80" y1="75" x2="80" y2="87" stroke="#0d2b57" stroke-width=".6"/>
  <circle cx="80" cy="70" r="7" fill="#0d2b57"/><path d="M77 72l5-5M80 67h2v2" stroke="#fff" stroke-width=".9" fill="none"/>
  <line x1="187" y1="75" x2="187" y2="87" stroke="#1c4f9c" stroke-width=".6"/>
  <circle cx="187" cy="70" r="7" fill="#0d2b57"/><rect x="183.5" y="67.5" width="7" height="5" fill="none" stroke="#fff" stroke-width=".8"/>
  <line x1="133" y1="95" x2="133" y2="108" stroke="#ef4b2a" stroke-width=".6"/>
  <circle cx="133" cy="113" r="7" fill="#ef4b2a"/><rect x="130" y="110" width="6" height="6" rx="1" fill="none" stroke="#fff" stroke-width=".8"/>
  <line x1="240" y1="95" x2="240" y2="108" stroke="#f7941d" stroke-width=".6"/>
  <circle cx="240" cy="113" r="7" fill="#f7941d"/><circle cx="240" cy="113" r="3" fill="none" stroke="#fff" stroke-width=".8"/>
  <g text-anchor="middle">
    <text x="133" y="54" font-size="3.6" font-weight="700" fill="#3c4250">Idea</text>
    <text x="133" y="59" class="tiny">Suitable for all kind business</text><text x="133" y="63" class="tiny">and personal presentation, feel</text><text x="133" y="67" class="tiny">free to add it this is your</text><text x="133" y="71" class="tiny">presentation.</text>
    <text x="240" y="54" font-size="3.6" font-weight="700" fill="#3c4250">Brainstorming</text>
    <text x="240" y="59" class="tiny">Suitable for all kind business</text><text x="240" y="63" class="tiny">and personal presentation, feel</text><text x="240" y="67" class="tiny">free to add it this is your</text><text x="240" y="71" class="tiny">presentation.</text>
    <text x="80" y="104" font-size="3.6" font-weight="700" fill="#3c4250">Research</text>
    <text x="80" y="109" class="tiny">Suitable for all kind business</text><text x="80" y="113" class="tiny">and personal presentation, feel</text><text x="80" y="117" class="tiny">free to add it this is your</text><text x="80" y="121" class="tiny">presentation.</text>
    <text x="187" y="104" font-size="3.6" font-weight="700" fill="#3c4250">Search</text>
    <text x="187" y="109" class="tiny">Suitable for all kind business</text><text x="187" y="113" class="tiny">and personal presentation, feel</text><text x="187" y="117" class="tiny">free to add it this is your</text><text x="187" y="121" class="tiny">presentation.</text>
  </g>
  <use href="#footer"/>
</svg>
</section>

<!-- Row 2 -->
<section class="slide c1 r2" aria-label="Five step process">
<svg viewBox="0 0 322 180">
  <use href="#tbar"/>
  <g font-size="3" fill="#fff" font-weight="700" text-anchor="middle">
    <path d="M27 87h46l4 3-4 3h-46z" fill="#ef4b2a"/><text x="50" y="91">Step Number One</text>
    <path d="M77 87h46l4 3-4 3h-46z" fill="#0d2b57"/><text x="100" y="91">Step Number Two</text>
    <path d="M127 87h46l4 3-4 3h-46z" fill="#f7941d"/><text x="150" y="91">Step Number Three</text>
    <path d="M177 87h46l4 3-4 3h-46z" fill="#0d2b57"/><text x="200" y="91">Step Number Three</text>
    <path d="M227 87h46l4 3-4 3h-46z" fill="#1c4f9c"/><text x="250" y="91">Step Number Four</text>
    <path d="M277 87h22v6h-22z" fill="#ef4b2a"/><text x="288" y="91">Step Five</text>
  </g>
  <g font-size="13" font-weight="900" text-anchor="middle">
    <text x="92" y="82" fill="#1c4f9c">02</text>
    <text x="185" y="82" fill="#f7941d">04</text>
    <text x="270" y="82" fill="#ef4b2a">04</text>
    <text x="47" y="114" fill="#ef4b2a">01</text>
    <text x="138" y="114" fill="#f7941d">03</text>
    <text x="224" y="114" fill="#0d2b57">05</text>
  </g>
  <g class="tiny" text-anchor="middle">
    <text x="52" y="72">Some short copy text</text><text x="52" y="76">to describe this step</text>
    <text x="230" y="72">Some short copy text</text><text x="230" y="76">to describe this step</text>
    <text x="92" y="100">Some short copy text</text><text x="92" y="104">to describe this step</text>
    <text x="180" y="100">Some short copy text</text><text x="180" y="104">to describe this step</text>
    <text x="270" y="100">Some short copy text</text><text x="270" y="104">to describe this step</text>
  </g>
  <use href="#footer"/>
</svg>
</section>

<section class="slide c2 r2" aria-label="India Map">
<svg viewBox="0 0 322 180">
  <use href="#tbar"/><text x="8" y="16.5" class="title">India Map</text>
  <rect x="95" y="28" width="115" height="135" rx="30" fill="#c9cdd3" role="img" aria-label="Map of India with highlighted regions"/>
  <g font-size="3" fill="#fff">
    <rect x="42" y="72" width="48" height="18" fill="#f7941d"/><text x="66" y="77" text-anchor="middle" font-weight="700">Branch 4</text><text x="66" y="82" text-anchor="middle">Location</text><text x="66" y="87" text-anchor="middle">+00 123 4567</text>
    <rect x="42" y="134" width="50" height="18" fill="#ef4b2a"/><text x="67" y="139" text-anchor="middle" font-weight="700">Branch 2</text><text x="67" y="144" text-anchor="middle">Location</text><text x="67" y="149" text-anchor="middle">+00 123 4567</text>
    <rect x="228" y="40" width="58" height="22" fill="#1c4f9c"/><text x="242" y="46" font-weight="700">Branch 3</text><text x="242" y="51">Location</text><text x="242" y="57">+00 123 4567</text>
    <rect x="210" y="118" width="58" height="22" fill="#0d2b57"/><text x="224" y="124" font-weight="700">Branch 1</text><text x="224" y="129">Location</text><text x="224" y="135">+00 123 4567</text>
  </g>
  <circle cx="220" cy="51" r="8" fill="#0d2b57" stroke="#fff" stroke-width="1"/>
  <circle cx="203" cy="129" r="8" fill="#0d2b57" stroke="#fff" stroke-width="1"/>
  <circle cx="100" cy="142" r="8" fill="#fff" stroke="#ef4b2a" stroke-width="1.5"/>
  <g stroke="#1c4f9c" stroke-width=".5" fill="none"><path d="M212 51l-25 20"/><path d="M195 129l-20-15"/></g>
  <use href="#footer"/>
</svg>
</section>

<section class="slide c3 r2" aria-label="North America Map">
<svg viewBox="0 0 322 180">
  <use href="#tbar"/><text x="8" y="16.5" class="title">North America Map</text>
  <text x="28" y="50" font-size="4" fill="#7a808c">Analysis</text>
  <text x="28" y="64" font-size="12" font-weight="900" fill="#ef4b2a">89%</text>
  <text x="72" y="54" class="tiny">Of shopping units are done via</text><text x="72" y="58" class="tiny">online channels with mobile use</text><text x="72" y="62" class="tiny">leading the way today.</text>
  <g>
    <rect x="28" y="82" width="110" height="4" fill="#e4e6ea"/><rect x="28" y="82" width="22" height="4" fill="#0d2b57"/><rect x="28" y="82" width="5" height="4" fill="#1c4f9c"/>
    <rect x="28" y="91" width="110" height="4" fill="#e4e6ea"/><rect x="28" y="91" width="60" height="4" fill="#ef4b2a"/><rect x="28" y="91" width="5" height="4" fill="#0d2b57"/>
    <rect x="28" y="100" width="110" height="4" fill="#e4e6ea"/><rect x="28" y="100" width="40" height="4" fill="#1c4f9c"/><rect x="28" y="100" width="5" height="4" fill="#0d2b57"/>
    <rect x="28" y="109" width="110" height="4" fill="#e4e6ea"/><rect x="28" y="109" width="90" height="4" fill="#f7941d"/><rect x="28" y="109" width="5" height="4" fill="#0d2b57"/>
    <rect x="28" y="118" width="110" height="4" fill="#e4e6ea"/><rect x="28" y="118" width="35" height="4" fill="#7fa13a"/><rect x="28" y="118" width="5" height="4" fill="#0d2b57"/>
  </g>
  <rect x="170" y="28" width="140" height="132" rx="25" fill="#d2d5da" role="img" aria-label="Map of North America"/>
  <circle cx="280" cy="45" r="11" fill="#1c4f9c"/><text x="280" y="47" font-size="4" fill="#fff" text-anchor="middle">30%</text>
  <circle cx="228" cy="88" r="7" fill="#f7941d"/><text x="228" y="90" font-size="3.4" fill="#fff" text-anchor="middle">25%</text>
  <circle cx="248" cy="118" r="14" fill="#ef4b2a"/><text x="248" y="120" font-size="5" fill="#fff" text-anchor="middle">75%</text>
  <use href="#footer"/>
</svg>
</section>

<!-- Row 3 -->
<section class="slide c1 r3" aria-label="Australia and New Zealand Map">
<svg viewBox="0 0 322 180">
  <use href="#tbar"/><text x="8" y="16.5" class="title">Australia &amp; New Zealand Map</text>
  <rect x="28" y="35" width="125" height="110" rx="30" fill="#c3c7cd" role="img" aria-label="Map of Australia and New Zealand with highlighted states"/>
  <g font-size="5" font-weight="700" fill="#fff">
    <text x="95" y="73">389K</text><text x="41" y="94">489K</text><text x="120" y="90">219K</text><text x="98" y="105">337K</text><text x="117" y="120">129K</text>
  </g>
  <circle cx="255" cy="68" r="22" fill="none" stroke="#e6e8ec" stroke-width="4"/>
  <circle cx="255" cy="68" r="22" fill="none" stroke="#0d2b57" stroke-width="4" stroke-dasharray="96 42" transform="rotate(-90 255 68)"/>
  <circle cx="255" cy="68" r="22" fill="none" stroke="#f7941d" stroke-width="4" stroke-dasharray="0 96 30 42" transform="rotate(-90 255 68)"/>
  <circle cx="255" cy="68" r="22" fill="none" stroke="#ef4b2a" stroke-width="4" stroke-dasharray="0 126 12 0" transform="rotate(-90 255 68)"/>
  <text x="255" y="71" font-size="9" font-weight="700" fill="#0d2b57" text-anchor="middle">12,3,00</text>
  <text x="222" y="106" font-size="3.4" fill="#f7941d">For every 5 emails received, we get 1 Phone calls</text>
  <text x="222" y="111" font-size="3.2" fill="#f7941d">Suitable for all categories business presentation.</text>
  <circle cx="224" cy="118" r="1.8" fill="#0d2b57"/><text x="228" y="119.3" class="tiny">Put your description</text>
  <circle cx="262" cy="118" r="1.8" fill="#f7941d"/><text x="266" y="119.3" class="tiny">Put your description</text>
  <circle cx="224" cy="125" r="1.8" fill="#ef4b2a"/><text x="228" y="126.3" class="tiny">Put your description</text>
  <use href="#footer"/>
</svg>
</section>

<section class="slide c2 r3" aria-label="6 Doughnut Chart">
<svg viewBox="0 0 322 180">
  <use href="#tbar"/><text x="8" y="16.5" class="title">6 Doughnut Chart</text>
  <g stroke-width="2.4" fill="none">
    <circle cx="52" cy="66" r="12" stroke="#e6e8ec"/><circle cx="52" cy="66" r="12" stroke="#0d2b57" stroke-dasharray="56.5 75.4" transform="rotate(-90 52 66)"/>
    <circle cx="155" cy="66" r="12" stroke="#e6e8ec"/><circle cx="155" cy="66" r="12" stroke="#1c4f9c" stroke-dasharray="67.8 75.4" transform="rotate(-90 155 66)"/>
    <circle cx="237" cy="66" r="12" stroke="#e6e8ec"/><circle cx="237" cy="66" r="12" stroke="#7fa13a" stroke-dasharray="26.4 75.4" transform="rotate(-90 237 66)"/>
    <circle cx="52" cy="119" r="12" stroke="#e6e8ec"/><circle cx="52" cy="119" r="12" stroke="#ef4b2a" stroke-dasharray="67.8 75.4" transform="rotate(-90 52 119)"/>
    <circle cx="155" cy="119" r="12" stroke="#e6e8ec"/><circle cx="155" cy="119" r="12" stroke="#f7941d" stroke-dasharray="52 75.4" transform="rotate(-90 155 119)"/>
    <circle cx="237" cy="119" r="12" stroke="#e6e8ec"/><circle cx="237" cy="119" r="12" stroke="#8a44a8" stroke-dasharray="52 75.4" transform="rotate(-90 237 119)"/>
  </g>
  <g font-size="7" text-anchor="middle">
    <text x="52" y="68.5" fill="#0d2b57">75%</text><text x="155" y="68.5" fill="#1c4f9c">90%</text><text x="237" y="68.5" fill="#7fa13a">35%</text>
    <text x="52" y="121.5" fill="#ef4b2a">90%</text><text x="155" y="121.5" fill="#f7941d">69%</text><text x="237" y="121.5" fill="#8a44a8">69%</text>
  </g>
  <line x1="118" y1="50" x2="118" y2="140" stroke="#e0e2e6" stroke-width=".5"/><line x1="213" y1="50" x2="213" y2="140" stroke="#e0e2e6" stroke-width=".5"/>
  <line x1="30" y1="92" x2="300" y2="92" stroke="#e0e2e6" stroke-width=".5"/>
  <g font-size="4.2" font-weight="700">
    <text x="68" y="62" fill="#0d2b57">Graphic Design</text><text x="170" y="62" fill="#1c4f9c">SEO Analysis</text><text x="253" y="62" fill="#7fa13a">Promotion</text>
    <text x="68" y="115" fill="#ef4b2a">Web Design</text><text x="170" y="115" fill="#f7941d">Marketing</text><text x="253" y="115" fill="#8a44a8">Video Editing</text>
  </g>
  <g class="tiny">
    <text x="68" y="67">Suitable for all category,</text><text x="68" y="71">Lorem Ipsum is not</text><text x="68" y="75">simply random text.</text>
    <text x="170" y="67">Suitable for all category,</text><text x="170" y="71">Lorem Ipsum is not</text><text x="170" y="75">simply random text.</text>
    <text x="253" y="67">Suitable for all category,</text><text x="253" y="71">Lorem Ipsum is not</text><text x="253" y="75">simply random text.</text>
    <text x="68" y="120">Suitable for all category,</text><text x="68" y="124">Lorem Ipsum is not</text><text x="68" y="128">simply random text.</text>
    <text x="170" y="120">Suitable for all category,</text><text x="170" y="124">Lorem Ipsum is not</text><text x="170" y="128">simply random text.</text>
    <text x="253" y="120">Suitable for all category,</text><text x="253" y="124">Lorem Ipsum is not</text><text x="253" y="128">simply random text.</text>
    <text x="30" y="159">We have organized and managed the Lorem ipsum just to make this Paragraph looks good by adding some English here and there. So, this is the real Lorem</text>
    <text x="30" y="163">ipsum dolor sit amet, consectetur adipisicing elit sed do eiusmod tempor incididunt ut labore et dolore magna aliqua.</text>
  </g>
  <use href="#footer"/>
</svg>
</section>

<section class="slide c3 r3" aria-label="Full Page Bar Chart">
<svg viewBox="0 0 322 180">
  <use href="#tbar"/><text x="8" y="16.5" class="title">Full Page Bar Chart</text>
  <g class="tiny" text-anchor="end">
    <text x="34" y="60">250%</text><text x="34" y="76">200%</text><text x="34" y="92">150%</text><text x="34" y="108">100%</text><text x="34" y="124">50%</text><text x="34" y="140">0%</text>
  </g>
  <line x1="38" y1="139" x2="300" y2="139" stroke="#ccd0d5" stroke-width=".5"/>
  <g>
    <rect x="44" y="133" width="3.5" height="6" fill="#0d2b57"/><rect x="48" y="129" width="3.5" height="10" fill="#1c4f9c"/><rect x="52" y="125" width="3.5" height="14" fill="#0d2b57"/>
    <rect x="66" y="131" width="3.5" height="8" fill="#0d2b57"/><rect x="70" y="122" width="3.5" height="17" fill="#1c4f9c"/>
    <rect x="86" y="120" width="3.5" height="19" fill="#1c4f9c"/><rect x="90" y="130" width="3.5" height="9" fill="#ef4b2a"/>
    <rect x="106" y="118" width="3.5" height="21" fill="#0d2b57"/><rect x="110" y="125" width="3.5" height="14" fill="#ef4b2a"/>
    <rect x="126" y="124" width="3.5" height="15" fill="#0d2b57"/><rect x="130" y="115" width="3.5" height="24" fill="#8a44a8"/><rect x="134" y="128" width="3.5" height="11" fill="#f7941d"/>
    <rect x="150" y="113" width="3.5" height="26" fill="#0d2b57"/><rect x="154" y="105" width="3.5" height="34" fill="#f7941d"/>
    <rect x="170" y="108" width="3.5" height="31" fill="#1c4f9c"/><rect x="174" y="117" width="3.5" height="22" fill="#7fa13a"/>
    <rect x="190" y="100" width="3.5" height="39" fill="#8a44a8"/><rect x="194" y="111" width="3.5" height="28" fill="#0d2b57"/>
    <rect x="210" y="104" width="3.5" height="35" fill="#0d2b57"/><rect x="214" y="95" width="3.5" height="44" fill="#f7941d"/>
    <rect x="230" y="92" width="3.5" height="47" fill="#1c4f9c"/><rect x="234" y="101" width="3.5" height="38" fill="#8a44a8"/>
    <rect x="250" y="100" width="3.5" height="39" fill="#0d2b57"/><rect x="254" y="88" width="3.5" height="51" fill="#7fa13a"/>
    <rect x="270" y="96" width="3.5" height="43" fill="#0d2b57"/><rect x="274" y="78" width="3.5" height="61" fill="#8a44a8"/>
  </g>
  <path d="M252 51h26v8h-11l-2 2-2-2h-11z" fill="#8a44a8"/>
  <text x="265" y="56.5" font-size="3.4" fill="#fff" text-anchor="middle">50% Growth</text>
  <g class="tiny" text-anchor="middle">
    <text x="50" y="145">Jan</text><text x="70" y="145">Feb</text><text x="90" y="145">Mar</text><text x="110" y="145">Apr</text><text x="130" y="145">May</text><text x="152" y="145">Jun</text><text x="172" y="145">Jul</text><text x="192" y="145">Aug</text><text x="212" y="145">Sep</text><text x="232" y="145">Oct</text><text x="252" y="145">Nov</text><text x="272" y="145">Dec</text>
    <text x="150" y="152">■ Series One ■ Series Two</text>
  </g>
  <use href="#footer"/>
</svg>
</section>

<!-- Row 4 -->
<section class="slide c1 r4" aria-label="Your Global Lead Partner">
<svg viewBox="0 0 322 180">
  <defs><linearGradient id="dusk" x1="0" y1="0" x2="0" y2="1"><stop offset="0" stop-color="#2d4d6e"/><stop offset=".6" stop-color="#4c6a86"/><stop offset="1" stop-color="#7a6a58"/></linearGradient></defs>
  <rect x="0" y="0" width="322" height="78" fill="url(#dusk)" role="img" aria-label="Photo of a city skyline at dusk"/>
  <rect x="0" y="0" width="133" height="78" fill="#0d2b57" opacity=".55"/>
  <text x="18" y="46" font-size="13" fill="#fff">Your Global</text>
  <text x="18" y="62" font-size="13" fill="#fff">Lead Parner</text>
  <rect x="0" y="78" width="133" height="102" fill="#1c4f9c"/>
  <rect x="133" y="78" width="94" height="102" fill="#f7941d"/>
  <rect x="227" y="78" width="95" height="102" fill="#7fa13a"/>
  <g stroke="#fff" fill="none" stroke-width="1">
    <circle cx="62" cy="104" r="9"/><ellipse cx="62" cy="104" rx="4" ry="9"/><line x1="53" y1="104" x2="71" y2="104"/>
    <circle cx="180" cy="104" r="6"/><circle cx="180" cy="104" r="2"/>
    <circle cx="274" cy="103" r="7"/><line x1="274" y1="110" x2="274" y2="116"/>
  </g>
  <g font-size="3.8" fill="#fff" text-anchor="middle">
    <text x="62" y="126">Your Text Here</text><text x="62" y="131">Lorem ipsum</text><text x="62" y="136">consectetur adipiscing</text><text x="62" y="141">elit.</text>
    <text x="180" y="126">Your Text Here</text><text x="180" y="131">Lorem ipsum</text><text x="180" y="136">consectetur adipiscing</text><text x="180" y="141">elit.</text>
    <text x="274" y="126">Your Text Here</text><text x="274" y="131">Lorem ipsum</text><text x="274" y="136">consectetur adipiscing</text><text x="274" y="141">elit.</text>
  </g>
</svg>
</section>

<section class="slide c2 r4" aria-label="Process Slide">
<svg viewBox="0 0 322 180">
  <use href="#tbar"/><text x="8" y="16.5" class="title">Process Slide</text>
  <g stroke="#0d2b57" stroke-width="1.2" fill="none">
    <path d="M50 155h50v-28h50v-28h50v-28h50v-28h50"/>
  </g>
  <g font-size="10" font-weight="700" fill="#0d2b57">
    <text x="52" y="151">01</text><text x="102" y="123">02</text><text x="152" y="95">03</text><text x="202" y="67">04</text>
  </g>
  <g class="tiny">
    <text x="66" y="143" fill="#3c4250">Your Text Here</text><text x="66" y="147">Lorem ipsum consectetur</text><text x="66" y="151">adipiscing elit.</text>
    <text x="116" y="115" fill="#3c4250">Your Text Here</text><text x="116" y="119">Lorem ipsum consectetur</text><text x="116" y="123">adipiscing elit.</text>
    <text x="166" y="87" fill="#3c4250">Your Text Here</text><text x="166" y="91">Lorem ipsum consectetur</text><text x="166" y="95">adipiscing elit.</text>
    <text x="216" y="59" fill="#3c4250">Your Text Here</text><text x="216" y="63">Lorem ipsum consectetur</text><text x="216" y="67">adipiscing elit.</text>
  </g>
  <g class="tiny">
    <text x="18" y="73" fill="#0d2b57" font-size="3.8">Lorem ipsum dolor sit amet</text>
    <text x="18" y="78">consectetur adipiscing elit, sed do</text><text x="18" y="82">eiusmod tempor incididunt ut labore et</text><text x="18" y="86">dolore magna aliqua ut enim ad</text><text x="18" y="90">minim veniam.</text>
    <text x="225" y="125" fill="#0d2b57" font-size="3.8">Lorem ipsum dolor sit amet,</text>
    <text x="225" y="130">consectetur adipiscing elit, sed do</text><text x="225" y="134">eiusmod tempor incididunt ut labore et</text><text x="225" y="138">dolore magna aliqua ut enim ad</text><text x="225" y="142">minim veniam.</text>
  </g>
  <use href="#footer"/>
</svg>
</section>

<section class="slide c3 r4" aria-label="Right Bar Chart">
<svg viewBox="0 0 322 180">
  <rect x="0" y="0" width="120" height="171" fill="#0d2b57"/>
  <text x="30" y="58" font-size="10" fill="#f7941d">Right</text>
  <text x="30" y="72" font-size="10" fill="#fff">Bar Chart</text>
  <text x="30" y="86" font-size="10" fill="#fff">Title Here</text>
  <g font-size="3" fill="#fff" opacity=".85" text-anchor="middle">
    <text x="67" y="116">Mauris quam dolor, cursus at porta</text><text x="67" y="120">et, luctus eget purus. Nunc tempor</text><text x="67" y="124">luctus interdum. Duis libero</text><text x="67" y="128">leo dignissim.</text>
  </g>
  <g>
    <rect x="150" y="47" width="5" height="42" fill="#0d2b57"/><rect x="157" y="64" width="5" height="25" fill="#ef4b2a"/>
    <rect x="190" y="73" width="5" height="16" fill="#0d2b57"/><rect x="197" y="69" width="5" height="20" fill="#f7941d"/><rect x="204" y="45" width="5" height="44" fill="#ef4b2a"/>
    <rect x="233" y="58" width="5" height="31" fill="#0d2b57"/><rect x="240" y="67" width="5" height="22" fill="#0d2b57"/><rect x="247" y="54" width="5" height="35" fill="#ef4b2a"/>
    <rect x="275" y="51" width="5" height="38" fill="#0d2b57"/><rect x="282" y="53" width="5" height="36" fill="#ef4b2a"/><rect x="289" y="43" width="5" height="46" fill="#f7941d"/>
  </g>
  <g class="tiny" text-anchor="middle"><text x="220" y="101">■ Data ■ Internet ■ Data</text></g>
  <text x="190" y="141" font-size="15" font-weight="700" fill="#ef4b2a" text-anchor="middle">85%</text>
  <text x="223" y="129" font-size="3.8" fill="#ef4b2a">Sales</text>
  <g class="tiny"><text x="223" y="134">Mauris quam dolor, cursus at</text><text x="223" y="138">porta et, luctus eget purus.</text><text x="223" y="142">Nunc tempor luctus interdum.</text><text x="223" y="146">Duis libero leo dignissim.</text></g>
  <use href="#footer"/>
</svg>
</section>

<!-- Row 5 -->
<section class="slide c1 r5" aria-label="Three Column Table">
<svg viewBox="0 0 322 180">
  <use href="#tbar"/><text x="8" y="16.5" class="title">Three Column Table</text>
  <g>
    <rect x="8" y="44" width="100" height="7" fill="#0d2b57"/>
    <rect x="8" y="53" width="100" height="8" fill="#e4e6ea"/>
    <rect x="8" y="63" width="100" height="84" fill="#f4f5f7"/>
    <rect x="8" y="63" width="13" height="84" fill="#0d2b57"/>
    <g stroke="#ffffff" stroke-width=".8"><line x1="8" y1="75" x2="108" y2="75"/><line x1="8" y1="87" x2="108" y2="87"/><line x1="8" y1="99" x2="108" y2="99"/><line x1="8" y1="111" x2="108" y2="111"/><line x1="8" y1="123" x2="108" y2="123"/><line x1="8" y1="135" x2="108" y2="135"/></g>
    <g font-size="2.6" fill="#7a808c" text-anchor="middle"><text x="35" y="72">16</text><text x="52" y="72">22</text><text x="69" y="72">18</text><text x="86" y="72">24</text><text x="101" y="72">30</text><text x="35" y="96">14</text><text x="52" y="96">35</text><text x="69" y="96">26</text><text x="86" y="96">16</text><text x="101" y="96">19</text><text x="35" y="120">28</text><text x="52" y="120">17</text><text x="69" y="120">32</text><text x="86" y="120">25</text><text x="101" y="120">21</text></g>
    <text x="58" y="49" font-size="3.2" fill="#fff" font-weight="700" text-anchor="middle">Your Table 1 Title Here</text>
  </g>
  <g transform="translate(104 0)">
    <rect x="8" y="44" width="100" height="7" fill="#0d2b57"/><rect x="8" y="53" width="100" height="8" fill="#e4e6ea"/><rect x="57" y="53" width="16" height="8" fill="#f7941d"/>
    <rect x="8" y="63" width="100" height="84" fill="#f4f5f7"/><rect x="8" y="63" width="13" height="84" fill="#0d2b57"/>
    <g stroke="#fff" stroke-width=".8"><line x1="8" y1="75" x2="108" y2="75"/><line x1="8" y1="87" x2="108" y2="87"/><line x1="8" y1="99" x2="108" y2="99"/><line x1="8" y1="111" x2="108" y2="111"/><line x1="8" y1="123" x2="108" y2="123"/><line x1="8" y1="135" x2="108" y2="135"/></g>
    <g font-size="2.6" fill="#7a808c" text-anchor="middle"><text x="35" y="72">21</text><text x="52" y="72">17</text><text x="69" y="72">30</text><text x="86" y="72">12</text><text x="101" y="72">26</text><text x="35" y="96">33</text><text x="52" y="96">24</text><text x="69" y="96">15</text><text x="86" y="96">29</text><text x="101" y="96">18</text><text x="35" y="120">20</text><text x="52" y="120">27</text><text x="69" y="120">11</text><text x="86" y="120">34</text><text x="101" y="120">23</text></g>
    <text x="58" y="49" font-size="3.2" fill="#fff" font-weight="700" text-anchor="middle">Your Table 2 Title Here</text>
  </g>
  <g transform="translate(208 0)">
    <rect x="8" y="44" width="100" height="7" fill="#0d2b57"/><rect x="8" y="53" width="100" height="8" fill="#e4e6ea"/>
    <rect x="8" y="63" width="100" height="84" fill="#f4f5f7"/><rect x="8" y="63" width="13" height="84" fill="#0d2b57"/>
    <g stroke="#fff" stroke-width=".8"><line x1="8" y1="75" x2="108" y2="75"/><line x1="8" y1="87" x2="108" y2="87"/><line x1="8" y1="99" x2="108" y2="99"/><line x1="8" y1="111" x2="108" y2="111"/><line x1="8" y1="123" x2="108" y2="123"/><line x1="8" y1="135" x2="108" y2="135"/></g>
    <g font-size="2.6" fill="#7a808c" text-anchor="middle"><text x="35" y="72">19</text><text x="52" y="72">28</text><text x="69" y="72">22</text><text x="86" y="72">15</text><text x="101" y="72">31</text><text x="35" y="96">25</text><text x="52" y="96">13</text><text x="69" y="96">36</text><text x="86" y="96">20</text><text x="101" y="96">27</text><text x="35" y="120">17</text><text x="52" y="120">32</text><text x="69" y="120">24</text><text x="86" y="120">19</text><text x="101" y="120">14</text></g>
    <text x="58" y="49" font-size="3.2" fill="#fff" font-weight="700" text-anchor="middle">Your Table 3 Title Here</text>
  </g>
  <use href="#footer"/>
</svg>
</section>

<section class="slide c2 r5" aria-label="3 Iterative Process">
<svg viewBox="0 0 322 180">
  <use href="#tbar"/><text x="8" y="16.5" class="title">3 Iterative Process</text>
  <g fill="none" stroke-width="14">
    <circle cx="160" cy="92" r="32" stroke="#ef4b2a" stroke-dasharray="62 139" transform="rotate(-80 160 92)"/>
    <circle cx="160" cy="92" r="32" stroke="#1c4f9c" stroke-dasharray="62 139" transform="rotate(40 160 92)"/>
    <circle cx="160" cy="92" r="32" stroke="#0d2b57" stroke-dasharray="62 139" transform="rotate(160 160 92)"/>
  </g>
  <circle cx="150" cy="58" r="6" fill="#fff" stroke="#0d2b57"/><circle cx="191" cy="100" r="6" fill="#fff" stroke="#ef4b2a"/><circle cx="135" cy="120" r="6" fill="#fff" stroke="#1c4f9c"/>
  <g font-size="3" fill="#fff" text-anchor="middle"><text x="180" y="72">Lorem Ipsum</text><text x="170" y="122">Lorem Ipsum</text><text x="136" y="85">Lorem Ipsum</text></g>
  <text x="215" y="63" font-size="4.2" fill="#ef4b2a">Segment Expansion</text>
  <g class="tiny"><text x="215" y="68">This Great Paragraph is a sample</text><text x="215" y="72">Lorem ipsum dolor sit amet,</text><text x="215" y="76">Consectetur adipiscing</text></g>
  <text x="218" y="126" font-size="4.2" fill="#1c4f9c">System Solution</text>
  <g class="tiny"><text x="218" y="131">This Great Paragraph is a sample</text><text x="218" y="135">Lorem ipsum dolor sit amet,</text><text x="218" y="139">Consectetur adipiscing</text></g>
  <text x="100" y="81" font-size="4.2" fill="#0d2b57" text-anchor="end">Time Management</text>
  <g class="tiny" text-anchor="end"><text x="100" y="86">This Great Paragraph is a sample</text><text x="100" y="90">Lorem ipsum dolor sit amet,</text><text x="100" y="94">Consectetur adipiscing</text></g>
  <use href="#footer"/>
</svg>
</section>

<section class="slide c3 r5" aria-label="4 Iterative Process">
<svg viewBox="0 0 322 180">
  <use href="#tbar"/><text x="8" y="16.5" class="title">4 Iterative Process</text>
  <g fill="none" stroke-width="14">
    <circle cx="160" cy="94" r="32" stroke="#ef4b2a" stroke-dasharray="47 154" transform="rotate(-175 160 94)"/>
    <circle cx="160" cy="94" r="32" stroke="#1c4f9c" stroke-dasharray="47 154" transform="rotate(-85 160 94)"/>
    <circle cx="160" cy="94" r="32" stroke="#f7941d" stroke-dasharray="47 154" transform="rotate(5 160 94)"/>
    <circle cx="160" cy="94" r="32" stroke="#0d2b57" stroke-dasharray="47 154" transform="rotate(95 160 94)"/>
  </g>
  <circle cx="150" cy="60" r="6" fill="#fff" stroke="#ef4b2a"/><circle cx="192" cy="86" r="6" fill="#fff" stroke="#1c4f9c"/><circle cx="170" cy="128" r="6" fill="#fff" stroke="#f7941d"/><circle cx="128" cy="104" r="6" fill="#fff" stroke="#0d2b57"/>
  <text x="100" y="62" font-size="4.2" fill="#ef4b2a" text-anchor="end">Money Management</text>
  <g class="tiny" text-anchor="end"><text x="100" y="67">This Great Paragraph is a sample</text><text x="100" y="71">Lorem ipsum dolor sit amet,</text><text x="100" y="75">Consectetur adipiscing</text></g>
  <text x="225" y="62" font-size="4.2" fill="#1c4f9c">System Upgrading</text>
  <g class="tiny"><text x="225" y="67">This Great Paragraph is a sample</text><text x="225" y="71">Lorem ipsum dolor sit amet,</text><text x="225" y="75">Consectetur adipiscing</text></g>
  <text x="100" y="132" font-size="4.2" fill="#0d2b57" text-anchor="end">Analysis</text>
  <g class="tiny" text-anchor="end"><text x="100" y="137">This Great Paragraph is a sample</text><text x="100" y="141">Lorem ipsum dolor sit amet,</text><text x="100" y="145">Consectetur adipiscing</text></g>
  <text x="225" y="132" font-size="4.2" fill="#f7941d">Time Management</text>
  <g class="tiny"><text x="225" y="137">This Great Paragraph is a sample</text><text x="225" y="141">Lorem ipsum dolor sit amet,</text><text x="225" y="145">Consectetur adipiscing</text></g>
  <use href="#footer"/>
</svg>
</section>

<!-- Row 6 -->
<section class="slide c1 r6" aria-label="6 Iterative Process">
<svg viewBox="0 0 322 180">
  <use href="#tbar"/><text x="8" y="16.5" class="title">6 Iterative Process</text>
  <g fill="none" stroke-width="15">
    <circle cx="160" cy="93" r="37" stroke="#8a44a8" stroke-dasharray="37 196" transform="rotate(-120 160 93)"/>
    <circle cx="160" cy="93" r="37" stroke="#7fa13a" stroke-dasharray="37 196" transform="rotate(-60 160 93)"/>
    <circle cx="160" cy="93" r="37" stroke="#f7941d" stroke-dasharray="37 196" transform="rotate(0 160 93)"/>
    <circle cx="160" cy="93" r="37" stroke="#1c4f9c" stroke-dasharray="37 196" transform="rotate(60 160 93)"/>
    <circle cx="160" cy="93" r="37" stroke="#ef4b2a" stroke-dasharray="37 196" transform="rotate(120 160 93)"/>
    <circle cx="160" cy="93" r="37" stroke="#0d2b57" stroke-dasharray="37 196" transform="rotate(180 160 93)"/>
  </g>
  <g fill="#fff"><circle cx="150" cy="57" r="7"/><circle cx="193" cy="76" r="7"/><circle cx="196" cy="116" r="7"/><circle cx="158" cy="131" r="7"/><circle cx="126" cy="112" r="7"/><circle cx="124" cy="76" r="7"/></g>
  <g font-size="3.2" fill="#fff" text-anchor="middle"><text x="174" y="64">Content</text><text x="200" y="96">Content</text><text x="182" y="130">Content</text><text x="140" y="133">Content</text></g>
  <g font-size="4" font-weight="700">
    <text x="70" y="60" fill="#0d2b57" text-anchor="end">Content 1</text>
    <text x="66" y="98" fill="#ef4b2a" text-anchor="end">Content 2</text>
    <text x="75" y="134" fill="#0d2b57" text-anchor="end">Content 3</text>
    <text x="228" y="125" fill="#f7941d">Content 4</text>
    <text x="240" y="87" fill="#7fa13a">Content 5</text>
    <text x="228" y="44" fill="#f7941d">Content 6</text>
  </g>
  <g class="tiny">
    <g text-anchor="end"><text x="70" y="65">Suitable for all category,</text><text x="70" y="69">Lorem Ipsum is not</text><text x="70" y="73">simply random text.</text>
    <text x="66" y="103">Suitable for all category,</text><text x="66" y="107">Lorem Ipsum is not</text><text x="66" y="111">simply random text.</text>
    <text x="75" y="139">Suitable for all category,</text><text x="75" y="143">Lorem Ipsum is not</text><text x="75" y="147">simply random text.</text></g>
    <text x="228" y="130">Suitable for all category,</text><text x="228" y="134">Lorem Ipsum is not</text><text x="228" y="138">simply random text.</text>
    <text x="240" y="92">Suitable for all category,</text><text x="240" y="96">Lorem Ipsum is not</text><text x="240" y="100">simply random text.</text>
    <text x="228" y="49">Suitable for all category,</text><text x="228" y="53">Lorem Ipsum is not</text><text x="228" y="57">simply random text.</text>
  </g>
  <use href="#footer"/>
</svg>
</section>

<section class="slide c2 r6" aria-label="Photo grid with descriptions">
<svg viewBox="0 0 322 180">
  <defs>
    <linearGradient id="sky1" x1="0" y1="0" x2="0" y2="1"><stop offset="0" stop-color="#6d7a86"/><stop offset="1" stop-color="#2f3b47"/></linearGradient>
    <linearGradient id="sky2" x1="0" y1="0" x2="1" y2="1"><stop offset="0" stop-color="#8d949b"/><stop offset="1" stop-color="#4a5560"/></linearGradient>
    <linearGradient id="sky3" x1="0" y1="0" x2="1" y2="1"><stop offset="0" stop-color="#c9d2dc"/><stop offset="1" stop-color="#6f7f92"/></linearGradient>
  </defs>
  <rect x="0" y="0" width="161" height="56" fill="#0d2b57"/>
  <rect x="161" y="0" width="161" height="56" fill="url(#sky1)" role="img" aria-label="Photo of a city skyline at twilight"/>
  <rect x="0" y="56" width="161" height="70" fill="url(#sky2)" role="img" aria-label="Aerial photo of dense city towers"/>
  <rect x="161" y="56" width="161" height="70" fill="#1c4f9c"/>
  <rect x="0" y="126" width="161" height="54" fill="#f7941d"/>
  <rect x="161" y="126" width="161" height="54" fill="url(#sky3)" role="img" aria-label="Photo of glass office facades"/>
  <g font-size="3.6" fill="#fff">
    <text x="12" y="10">Lorem ipsum dolor sit amet</text><text x="12" y="15">consectetur adipiscing elit, sed do eiusmod tempor</text><text x="12" y="20">incididunt ut labore et dolore magna aliqua. Ut</text><text x="12" y="25">enim ad minim veniam, quis nostrud exercitation</text><text x="12" y="30">ullamco laboris nisi ut aliquip ex ea commodo</text><text x="12" y="35">consequat.</text>
    <text x="173" y="77">Lorem ipsum dolor sit amet</text><text x="173" y="82">consectetur adipiscing elit, sed do eiusmod tempor</text><text x="173" y="87">incididunt ut labore et dolore magna aliqua. Ut</text><text x="173" y="92">enim ad minim veniam, quis nostrud exercitation</text><text x="173" y="97">ullamco laboris nisi ut aliquip ex ea commodo</text><text x="173" y="102">consequat.</text>
    <text x="12" y="135">Lorem ipsum dolor sit amet</text><text x="12" y="140">consectetur adipiscing elit, sed do eiusmod tempor</text><text x="12" y="145">incididunt ut labore et dolore magna aliqua. Ut</text><text x="12" y="150">enim ad minim veniam, quis nostrud exercitation</text><text x="12" y="155">ullamco laboris nisi ut aliquip ex ea commodo</text><text x="12" y="160">consequat.</text>
  </g>
</svg>
</section>

<section class="slide c3 r6" aria-label="Three Picture With Description">
<svg viewBox="0 0 322 180">
  <defs>
    <linearGradient id="aer" x1="0" y1="0" x2="1" y2="1"><stop offset="0" stop-color="#5b6a78"/><stop offset="1" stop-color="#2b3642"/></linearGradient>
    <linearGradient id="nite" x1="0" y1="0" x2="0" y2="1"><stop offset="0" stop-color="#3f5d84"/><stop offset="1" stop-color="#8a6a48"/></linearGradient>
  </defs>
  <use href="#tbar"/><text x="8" y="16.5" class="title">Three Picture With Description</text>
  <rect x="24" y="44" width="88" height="48" fill="url(#aer)" role="img" aria-label="Aerial photo of a city"/>
  <rect x="118" y="44" width="88" height="48" fill="#f7941d"/>
  <rect x="212" y="44" width="88" height="48" fill="url(#aer)" role="img" aria-label="Aerial photo of city streets"/>
  <rect x="24" y="97" width="88" height="48" fill="#0d2b57"/>
  <rect x="118" y="97" width="88" height="48" fill="url(#nite)" role="img" aria-label="Photo of a city skyline at night"/>
  <rect x="212" y="97" width="88" height="48" fill="#1c4f9c"/>
  <g fill="#fff">
    <text x="124" y="53" font-size="4.4" font-weight="700">Heading Goes Here</text>
    <text x="30" y="106" font-size="4.4" font-weight="700">Heading Goes Here</text>
    <text x="218" y="106" font-size="4.4" font-weight="700">Heading Goes Here</text>
    <g font-size="3.2">
      <text x="124" y="60">Lorem ipsum dolor sit amet, consectetur</text><text x="124" y="64">adipiscing elit, sed do eiusmod tempor</text><text x="124" y="68">incididunt ut labore et commodo</text><text x="124" y="72">consequat dolore magna aliqua.</text>
      <text x="30" y="113">Lorem ipsum dolor sit amet, consectetur</text><text x="30" y="117">adipiscing elit, sed do eiusmod tempor</text><text x="30" y="121">incididunt ut labore et commodo</text><text x="30" y="125">consequat dolore magna aliqua.</text>
      <text x="218" y="113">Lorem ipsum dolor sit amet, consectetur</text><text x="218" y="117">adipiscing elit, sed do eiusmod tempor</text><text x="218" y="121">incididunt ut labore et commodo</text><text x="218" y="125">consequat dolore magna aliqua.</text>
    </g>
  </g>
  <use href="#footer"/>
</svg>
</section>

<!-- Row 7 -->
<section class="slide c1 r7" aria-label="Topic cluster page with photo">
<svg viewBox="0 0 322 180">
  <defs><linearGradient id="city" x1="0" y1="0" x2="1" y2="1"><stop offset="0" stop-color="#7f8a95"/><stop offset=".5" stop-color="#4d5863"/><stop offset="1" stop-color="#2b333c"/></linearGradient></defs>
  <rect x="0" y="0" width="322" height="180" fill="url(#city)" role="img" aria-label="Aerial photo of a modern city district"/>
  <rect x="30" y="0" width="170" height="180" fill="#0d2b57" opacity=".82"/>
  <g font-size="13" fill="#fff" text-anchor="end">
    <text x="175" y="82">This Is Your</text><text x="175" y="99">Topic Cluster</text><text x="175" y="116">Page</text>
  </g>
</svg>
</section>

<section class="slide c2 r7" aria-label="Topic cluster page navy">
<svg viewBox="0 0 322 180">
  <rect x="0" y="0" width="322" height="180" fill="#0d2b57"/>
  <g font-size="13" fill="#fff" text-anchor="end">
    <text x="178" y="82">This Is Your</text><text x="178" y="99">Topic Cluster</text><text x="178" y="116">Page</text>
  </g>
  <line x1="194" y1="78" x2="194" y2="102" stroke="#ffffff" stroke-width=".6" opacity=".5"/>
  <text x="204" y="93" font-size="8" fill="#fff">Bright Towns Alliance</text>
</svg>
</section>

<section class="slide c3 r7" aria-label="Topic cluster page red">
<svg viewBox="0 0 322 180">
  <rect x="0" y="0" width="322" height="180" fill="#ef4b2a"/>
  <g font-size="13" fill="#fff" text-anchor="middle">
    <text x="161" y="88">This Is Your Topic</text><text x="161" y="105">Cluster Page</text>
  </g>
</svg>
</section>

<!-- Row 8 -->
<section class="slide c2 r8" aria-label="Topic cluster page orange">
<svg viewBox="0 0 322 180" preserveAspectRatio="none">
  <rect x="0" y="0" width="322" height="180" fill="#f7941d"/>
  <g font-size="13" fill="#fff" text-anchor="middle">
    <text x="161" y="88">This Is Your Topic</text><text x="161" y="105">Cluster Page</text>
  </g>
</svg>
</section>
</body>
</html>
```